Counseling business card, clean but alluring

I need it to appeal to all ages and men. I’m planning to use my current logo. I like crisp and clean. Possibly some shimmer. My website is harborleafcare.com
Updates

Contact Information for Business Card

Melissa "Missy" Dane Whitcomb, LPC-S, RPT-S

harborleafcare.com

28519 Thornbury Lane, Suite 406
Addison TX 75218

720-315-2984 | missy@harborleafcare.com

Colors
0355a3
85cae6
fbee3e
ffffff
33b8a4
0692cd

Requirements
Must have
• My logo

```html
<!DOCTYPE html>
<html lang="en">
<head>
<meta charset="utf-8">
<title>Harbor Leaf Care – Business Card</title>
<link rel="stylesheet" href="https://fonts.googleapis.com/css2?family=Josefin+Sans:wght@300&family=Lato:wght@400&display=swap">
<style>
  :root {
    --page-bg: #e9eaec;
    --card-dark: #050505;
    --card-light: #ffffff;
    --gold: #d9a44e;
    --gold-deep: #8a5a1c;
    --gold-pale: #f3d9a0;
    --blue: #4a7fd4;
    --blue-soft: #a9c6ee;
    --blue-pale: #dde9f8;
    --ink: #4d4d4d;
    --ink-soft: #6b6b6b;
  }
  * { box-sizing: border-box; margin: 0; padding: 0; }
  html, body { width: 1200px; height: 1200px; overflow: hidden; }
  body {
    background: var(--page-bg);
    font-family: "Lato", sans-serif;
    position: relative;
  }
  .card {
    position: absolute;
    left: 160px;
    width: 880px;
    height: 536px;
    overflow: hidden;
    box-shadow: 0 6px 20px rgba(0,0,0,0.18);
  }
  .card--front { top: 46px; background: var(--card-dark); border: 8px solid #fff; }
  .card--back { top: 618px; background: var(--card-light); border-radius: 6px; }

  /* nest artwork areas */
  .nest-art { position: absolute; border-radius: 50%; }
  .card--front .nest-art {
    width: 400px; height: 400px;
    right: -60px; top: -150px;
    background: radial-gradient(circle at 55% 55%, var(--gold-pale) 0%, var(--gold) 35%, var(--gold-deep) 62%, transparent 70%);
    opacity: 0.75;
  }
  .card--back .nest-art {
    width: 420px; height: 420px;
    right: -70px; top: -140px;
    background: radial-gradient(circle at 55% 55%, var(--blue-pale) 0%, var(--blue-soft) 40%, var(--blue) 60%, transparent 68%);
    opacity: 0.7;
  }
  .nest-rings { position: absolute; pointer-events: none; }
  .card--front .nest-rings { right: -80px; top: -170px; }
  .card--back .nest-rings { right: -90px; top: -160px; }

  /* brand name */
  .brand {
    position: absolute;
    display: flex;
    align-items: center;
    gap: 14px;
    font-family: "Josefin Sans", sans-serif;
    font-weight: 300;
    white-space: nowrap;
  }
  .brand__dot { border-radius: 50%; flex: none; }
  .card--front .brand { left: 96px; bottom: 84px; font-size: 60px; color: var(--gold); }
  .card--front .brand__dot { width: 26px; height: 26px; background: var(--gold); }
  .card--back .brand { right: 70px; bottom: 80px; font-size: 30px; color: var(--blue); }
  .card--back .brand__dot { width: 16px; height: 16px; background: var(--blue); }

  /* back card details */
  .identity { position: absolute; left: 84px; top: 108px; }
  .identity__name { font-size: 23px; color: var(--blue); }
  .identity__creds { font-size: 16px; color: var(--ink-soft); margin-left: 6px; }
  .identity__title { font-size: 13.5px; color: var(--ink); margin-top: 4px; }

  .contacts { position: absolute; left: 72px; top: 248px; list-style: none; }
  .contact { display: flex; align-items: flex-start; gap: 12px; margin-bottom: 20px; }
  .contact__icon {
    width: 24px; height: 24px; border-radius: 50%;
    background: var(--blue); flex: none; margin-top: 2px;
    display: flex; align-items: center; justify-content: center;
  }
  .contact__text { font-size: 20px; line-height: 1.3; color: var(--ink); }
</style>
</head>
<body>

<section class="card card--front" aria-label="Card front">
  <div class="nest-art" role="img" aria-label="Gold leafy branch nest illustration"></div>
  <svg class="nest-rings" width="440" height="440" viewBox="0 0 440 440" aria-hidden="true">
    <circle cx="220" cy="220" r="200" fill="none" stroke="var(--gold)" stroke-width="1.5"/>
    <circle cx="214" cy="226" r="210" fill="none" stroke="var(--gold)" stroke-width="1"/>
    <circle cx="226" cy="214" r="192" fill="none" stroke="var(--gold-pale)" stroke-width="1"/>
  </svg>
  <div class="brand"><span class="brand__dot"></span>Harbor Leaf Care</div>
</section>

<section class="card card--back" aria-label="Card back">
  <div class="nest-art" role="img" aria-label="Blue leafy branch nest illustration"></div>
  <svg class="nest-rings" width="460" height="460" viewBox="0 0 460 460" aria-hidden="true">
    <circle cx="230" cy="230" r="212" fill="none" stroke="var(--blue)" stroke-width="1.5"/>
    <circle cx="236" cy="236" r="222" fill="none" stroke="#d6d6d6" stroke-width="2"/>
    <circle cx="224" cy="224" r="204" fill="none" stroke="var(--blue-soft)" stroke-width="1"/>
  </svg>

  <div class="identity">
    <p><span class="identity__name">Melissa Dane Whitcomb</span><span class="identity__creds">LPC-S, RPT-S</span></p>
    <p class="identity__title">Counselor and Registered Play Therapist.</p>
  </div>

  <ul class="contacts">
    <li class="contact">
      <span class="contact__icon">
        <svg width="14" height="14" viewBox="0 0 24 24" aria-hidden="true"><path d="M6.6 10.8a15 15 0 0 0 6.6 6.6l2.2-2.2a1 1 0 0 1 1-.25 11.4 11.4 0 0 0 3.6.57 1 1 0 0 1 1 1V20a1 1 0 0 1-1 1A17 17 0 0 1 3 4a1 1 0 0 1 1-1h3.5a1 1 0 0 1 1 1c0 1.25.2 2.45.57 3.57a1 1 0 0 1-.25 1z" fill="#fff"/></svg>
      </span>
      <span class="contact__text">720-315-2984</span>
    </li>
    <li class="contact">
      <span class="contact__icon">
        <svg width="14" height="14" viewBox="0 0 24 24" aria-hidden="true" fill="none" stroke="#fff" stroke-width="2"><circle cx="12" cy="12" r="9"/><path d="M3 12h18M12 3c3 3 3 15 0 18M12 3c-3 3-3 15 0 18"/></svg>
      </span>
      <span class="contact__text">missy@harborleafcare.com<br>www.harborleafcare.com</span>
    </li>
    <li class="contact">
      <span class="contact__icon">
        <svg width="14" height="14" viewBox="0 0 24 24" aria-hidden="true"><circle cx="12" cy="12" r="7" fill="none" stroke="#fff" stroke-width="3"/><circle cx="12" cy="12" r="2.5" fill="#fff"/></svg>
      </span>
      <span class="contact__text">28519 Thornbury Lane<br>Suite 406 Lakewood CO<br>80226</span>
    </li>
  </ul>

  <div class="brand"><span class="brand__dot"></span>Harbor Leaf Care</div>
</section>

</body>
</html>
```